Freelance film producer/editor wants you to gleam nova!

'Gleam Nova' is my production business based in Melbourne, though I do a fair bit of work overseas. I'm a one woman show most of the time but enlist other crew members for larger projects. I manage productions from start to finish including producing, filming, editing, distribution, photography and animation.

My current tag line and details are as follows:

Petra Vandoren
Producer. Editor. Thinker.
[M] +61 492 157 630
[E] pv[at]brightpanel.com.au
www.brightpanel.com.au

I have a fairly wicked sense of humour and love a good pun, so feel free to work this into your design!

The final designs should demonstrate the areas I work in but not limited to. I'd rather not use old and typical "film" looking elements such as a clapper or negative reel. Having said that, the logo itself (attached) is quite typical because the first 'o' is a closed aperture and the second is a wide aperture. Happy for the logo to be pulled apart for the business card to be more interesting.

The majority of projects I work on are quite different and in some cases a bit crazy. Lots of travel involved. The main difference between me and other producers is that I don't say I work in 'film', even though i do. I want the card to leave me open to new roles and projects as opposed to squashing myself into one particular category.

I'm open to colour but prefer a simple design that isn't too hectic.

I have also attached an example I did like that was printed on plastic but then I realised so many other people had ripped it off....

I'm open to paper board or plastic (transparent) designs etc. One sided or two sided.

Thanks for sharing your ideas with me and please, go as nuts as you want to with this! :)

Target Market(s)

My clients range from non profits in health and educational institutions to record labels and well known artists. The business attracts corporates as well though the majority of my business is achieved through referral and word of mouth so most people will soon realise that my personality and work are very much intertwined and the reason they hire me for a job.

Industry/Entity Type

Business

Font styles to use
Other font styles liked:
• Eurostile or similar

Requirements
Must have
• I have a very open mind when it comes to design. I do like the existing tag line but if you can come up with something better I'm all ears! (and eyes)

Nice to have
• Back of the business card can be graphics, there can be transparent elements or holes, embossing options...
Should not have
• Besides my name, nothing should scream "I am woman!" because in my industry that's not a selling point.

The colour pink is a definite no.

```html
<!DOCTYPE html>
<html lang="en">
<head>
<meta charset="utf-8">
<title>Gleam Nova – Business Cards</title>
<link rel="stylesheet" href="https://fonts.googleapis.com/css2?family=Open+Sans:wght@300;400&display=swap">
<style>
  :root {
    --backdrop: #d9d9d9;
    --card-top: #1c1c1c;
    --card-bottom: #050505;
    --disc: #2a2a2a;
    --ink: #ffffff;
    --ink-soft: #cfcfcf;
  }
  * { margin: 0; padding: 0; box-sizing: border-box; }
  html, body {
    width: 1200px;
    height: 900px;
    overflow: hidden;
    background: var(--backdrop);
    font-family: "Open Sans", Arial, sans-serif;
  }
  .canvas { position: relative; width: 1200px; height: 900px; }

  .card {
    position: absolute;
    width: 540px;
    height: 310px;
    background: linear-gradient(160deg, var(--card-top) 0%, var(--card-bottom) 70%);
    color: var(--ink);
    overflow: hidden;
  }
  .card--front { left: 580px; top: 120px; }
  .card--back  { left: 80px;  top: 470px; }

  .disc {
    border-radius: 50%;
    background: var(--disc);
    flex: none;
  }

  /* front */
  .wordmark {
    position: absolute;
    left: 50px;
    top: 84px;
    height: 120px;
    display: flex;
    align-items: center;
    gap: 14px;
    font-weight: 300;
    font-size: 46px;
    letter-spacing: 1px;
    color: var(--ink);
    line-height: 1;
  }
  .wordmark .disc { width: 120px; height: 120px; }
  .card--front .web {
    position: absolute;
    right: 70px;
    bottom: 58px;
    font-size: 11px;
    letter-spacing: 6px;
    color: var(--ink-soft);
  }

  /* back */
  .card--back .disc {
    position: absolute;
    width: 130px;
    height: 130px;
    left: 205px;
    top: 80px;
  }
  .holder {
    position: absolute;
    left: 112px;
    top: 36px;
  }
  .holder__name {
    font-size: 15px;
    letter-spacing: 6px;
    text-transform: uppercase;
    font-weight: 400;
  }
  .holder__role {
    font-size: 10px;
    color: var(--ink-soft);
    margin-left: 72px;
    margin-top: 1px;
  }
  .contact {
    position: absolute;
    left: 40px;
    right: 40px;
    bottom: 34px;
    display: flex;
    justify-content: space-between;
    font-size: 11px;
    letter-spacing: 0.5px;
    color: var(--ink);
  }
  .contact__sep { color: var(--ink-soft); }
</style>
</head>
<body>
  <main class="canvas">
    <section class="card card--front" aria-label="Card front">
      <h1 class="wordmark">
        <span>gleam</span>
        <span class="disc" aria-hidden="true"></span>
        <span>nova</span>
      </h1>
      <p class="web">www.brightpanel.com.au</p>
    </section>

    <section class="card card--back" aria-label="Card back">
      <div class="disc" aria-hidden="true"></div>
      <div class="holder">
        <h2 class="holder__name">Petra Vandoren</h2>
        <p class="holder__role">Producer.Editor.Thinker</p>
      </div>
      <p class="contact">
        <span>+61 492 157 630</span>
        <span class="contact__sep">|</span>
        <span>pv@brightpanel.com.au</span>
        <span class="contact__sep">|</span>
        <span>www.brightpanel.com.au</span>
      </p>
    </section>
  </main>
</body>
</html>
```